Summer Resolution Do it Now

I run a hypnotherapy practice that helps people
Loose Weight,Stop smoking ,overcome fear of Public speaking and improve Confidence and positive attitude.
I like to market a especific group in the CBD Melbourne as I only practice once a week in the city.

I have some photographs that will go well for the flyer what I am after is something very professional ,sober and elegant.

Target Market(s)

CBD corporate Melbourne market 25 till 60 year old

Industry/Entity Type

Hypnotherapy

Requirements
Must have
• flyer should be two sided , must have http://www.calmtrancestudio.example/ and the phone number 0491627058 and encourage to book online .

```html
<!DOCTYPE html>
<html lang="en">
<head>
<meta charset="utf-8">
<title>Calm Trance Studio – Two-Sided Flyer</title>
<link rel="stylesheet" href="https://fonts.googleapis.com/css2?family=Source+Sans+3:wght@400;600;700&display=swap">
<style>
  :root {
    --brand-blue: #1b8fd8;
    --frame-blue: #2a90d6;
    --ink: #1c1c1c;
    --paper: #ffffff;
    --photo-shirt: #b9cde3;
    --photo-skin: #c9a58b;
    --photo-dark: #5b5f6a;
  }
  * { margin: 0; padding: 0; box-sizing: border-box; }
  html, body { width: 1200px; height: 900px; overflow: hidden; background: var(--paper); }
  body { position: relative; font-family: "Source Sans 3", Arial, sans-serif; color: var(--ink); }

  .flyer-side {
    position: absolute; top: 100px; width: 406px; height: 690px;
    border: 1.5px solid var(--frame-blue); background: var(--paper);
  }
  .flyer-side--front { left: 76px; }
  .flyer-side--back { left: 673px; }

  .top-rule {
    position: absolute; left: 0; top: 37px; width: 306px; height: 1.5px; background: var(--frame-blue);
  }
  .footer-rule {
    position: absolute; right: 0; top: 573px; width: 254px; height: 1.5px; background: var(--frame-blue);
  }

  .photo { position: absolute; }
  .photo--therapist {
    left: 32px; top: 45px; width: 104px; height: 111px;
    background: linear-gradient(180deg, #e9e4e0 0%, var(--photo-skin) 35%, var(--photo-shirt) 60%, #a9c0da 100%);
  }
  .photo--client {
    left: 32px; top: 39px; width: 96px; height: 169px;
    background: linear-gradient(180deg, #7a5640 0%, var(--photo-skin) 40%, var(--photo-dark) 75%, #4a4e58 100%);
  }

  .therapist-name {
    position: absolute; left: 31px; top: 165px;
    font-size: 13px; font-weight: 700; color: var(--brand-blue);
  }
  .body-copy {
    position: absolute; left: 31px; font-size: 13px; line-height: 17px; font-weight: 400;
  }
  .file-label { top: 200px; }
  .credentials { top: 234px; }
  .about { top: 335px; }

  .help-list {
    position: absolute; left: 135px; top: 77px; list-style: none;
    font-size: 12px; line-height: 23px;
  }
  .help-list .plus { color: var(--brand-blue); margin-right: 3px; }

  .testimonial { position: absolute; left: 31px; font-size: 12px; line-height: 23px; }
  .testimonial--one { top: 216px; }
  .testimonial--two { top: 336px; }
  .testimonial .quote-mark { color: var(--brand-blue); }
  .testimonial-name {
    display: block; font-size: 20px; font-weight: 700; color: var(--brand-blue); line-height: 24px; margin-top: 1px;
  }

  .locations { position: absolute; left: 31px; top: 454px; font-size: 12px; line-height: 23px; }
  .locations-title { font-size: 20px; font-weight: 700; color: var(--brand-blue); line-height: 26px; margin-bottom: 2px; }

  .brand-lockup { position: absolute; left: 40px; top: 560px; display: flex; align-items: flex-start; }
  .brand-dot { width: 92px; height: 92px; border-radius: 50%; background: var(--brand-blue); margin-top: 2px; }
  .brand-text { margin-left: 17px; margin-top: 20px; }
  .brand-name { font-size: 15px; font-weight: 400; color: var(--ink); line-height: 17px; }
  .brand-contact { font-size: 9.5px; color: var(--brand-blue); line-height: 12px; margin-top: 18px; letter-spacing: 0.6px; }
</style>
</head>
<body>

  <section class="flyer-side flyer-side--front">
    <div class="top-rule"></div>
    <div class="photo photo--therapist" role="img" aria-label="Portrait photograph of the hypnotherapist in a light blue shirt"></div>
    <h2 class="therapist-name">Daniel Whitford</h2>
    <p class="body-copy file-label">Daniel WhitfordPortrait.fw</p>
    <p class="body-copy credentials">
      Qualified Clinical Hypnotherapist<br>
      Institute of Clinical Trance (Accredited)<br>
      Member National Hypnotherapy Guild<br>
      Provider Number: NHG482167<br>
      HealthCover Provider Number: HCP0315872K
    </p>
    <p class="body-copy about">
      Hypnotherapy is a powerful tool and can assist<br>
      you in making desired changes to your life.<br>
      Daniel Whitford is a Clinical Hypnotherapist based<br>
      in Melbourne’s CBD and Western Suburbs (Footscray).<br>
      People from all over Australia come to see Daniel for<br>
      hypnotherapy consultations. You can book an<br>
      appointment online .&nbsp; Alternatively, you can call<br>
      0491 627 058 to enquire or to book an appointment.
    </p>
    <div class="footer-rule"></div>
    <div class="brand-lockup">
      <div class="brand-dot"></div>
      <div class="brand-text">
        <p class="brand-name">Calm Trance Studio</p>
        <p class="brand-contact">www.calmtrancestudio.example<br>0491627058</p>
      </div>
    </div>
  </section>

  <section class="flyer-side flyer-side--back">
    <div class="top-rule"></div>
    <div class="photo photo--client" role="img" aria-label="Photograph of a smiling professional woman in a grey shirt"></div>
    <ul class="help-list">
      <li>We can help you:</li>
      <li><span class="plus">+</span>Loose Weight,</li>
      <li><span class="plus">+</span>Stop smoking ,</li>
      <li><span class="plus">+</span>Overcome fear of Public speaking</li>
      <li><span class="plus">+</span>Improve Confidence and positive attitude</li>
    </ul>
    <blockquote class="testimonial testimonial--one">
      <span class="quote-mark">‘</span>I have been assisted by Daniel in number of ways.<br>
      I came in wanting help with my weight and health and<br>
      have left feeling I can take over the world<span class="quote-mark">’</span>
      <cite class="testimonial-name">Rosalind</cite>
    </blockquote>
    <blockquote class="testimonial testimonial--two">
      <span class="quote-mark">‘</span>I have had 5 sessions with Daniel and I feel good<br>
      about myself and very confident that I will succeed.<br>
      &nbsp;It has helped me a lot. Thank You Daniel<span class="quote-mark">’</span>
      <cite class="testimonial-name">Janine</cite>
    </blockquote>
    <div class="locations">
      <h3 class="locations-title">locations</h3>
      <p>Harbour Wellness 14/62 Lantern Lane,<br>
      Melbourne CBD (Wednesday Only)<br>
      Westgate Osteo 318 Fernhill Road, Footscray</p>
    </div>
    <div class="footer-rule"></div>
    <div class="brand-lockup">
      <div class="brand-dot"></div>
      <div class="brand-text">
        <p class="brand-name">Calm Trance Studio</p>
        <p class="brand-contact">www.calmtrancestudio.example<br>0491627058</p>
      </div>
    </div>
  </section>

</body>
</html>
```